Bus Card and Materials for Handyman and Landscaping
TLCard and Material
Bus Card and Materials for Handyman and Landscaping - Construction
Creative Brief
Professional
TL Handymand and Landscaping
Owner
PO Box 8172 Hilo, Hawaii 96738
tlenz8172@mailvexa.com
Insured
I'd like to use my business card also as a magnet for my car or yard signs. I like the colors but are also open to other colors that designers use through their creativity.
One side of the card with my information the other side for marketing purposes, logo or other images, designers - please continue to use your creativity to come up with stunning designs. Thank you
TLenz TLenz
Designers! Love the designs! I'd like to list the type of work I so on the back side or on the side of the card (use your creativity, its great!): Roof Restoration Cutting Trees Roofing Yard Maintenance Painting Yard Service (weekly, bi-monthly, monthly) Pressure Washing Extensions Building Restoration Drywall & Texture Concrete Work
Welcome designers! I'm excited to view your creative cutting edge designs for my business card, stationary, car magnet, and yard signs. Good luck to you all.

```html
<!DOCTYPE html>
<html lang="en">
<head>
<meta charset="utf-8">
<title>TL Handymand and Landscaping – Business Card</title>
<link href="https://fonts.googleapis.com/css2?family=Montserrat:wght@400;600;800&display=swap" rel="stylesheet">
<style>
  :root {
    --bg: #5e6063;
    --green: #1f8a3b;
    --green-dark: #0f6a2a;
    --green-light: #3fae4c;
    --ink: #222;
    --grey-text: #555;
    --white: #ffffff;
  }
  * { box-sizing: border-box; margin: 0; padding: 0; }
  html, body { width: 1200px; height: 876px; overflow: hidden; }
  body {
    background: var(--bg);
    font-family: "Montserrat", sans-serif;
    position: relative;
  }
  .card {
    position: absolute;
    top: 295px;
    width: 500px;
    height: 286px;
    border-radius: 4px;
    overflow: hidden;
    box-shadow: 0 10px 24px rgba(0,0,0,.35);
  }
  /* Front: contact side */
  .card-front { left: 70px; background: var(--white); }
  .contact { position: absolute; left: 34px; top: 32px; }
  .contact-name {
    color: var(--green);
    font-weight: 800;
    font-size: 19px;
    letter-spacing: .5px;
  }
  .contact-role { font-size: 11px; color: var(--grey-text); margin-top: 3px; }
  .contact-lines {
    list-style: none;
    margin-top: 26px;
    font-size: 11.5px;
    line-height: 1.6;
    color: var(--ink);
  }
  .front-brand {
    position: absolute;
    right: 30px;
    top: 132px;
    text-align: right;
  }
  .brand-name {
    display: flex;
    align-items: center;
    gap: 8px;
    font-weight: 800;
    font-size: 18px;
    line-height: 1.15;
    color: var(--green);
  }
  .brand-mark { width: 14px; height: 14px; background: var(--green); flex: none; }
  .brand-tagline {
    margin-top: 6px;
    font-size: 8px;
    letter-spacing: 2px;
    color: var(--grey-text);
  }
  .front-band {
    position: absolute;
    left: 0; right: 0; bottom: 0;
    height: 34px;
    background: linear-gradient(90deg, var(--green-dark), var(--green));
  }
  /* Back: marketing side */
  .card-back {
    left: 630px;
    background: radial-gradient(circle at 40% 30%, var(--green-light), var(--green) 45%, var(--green-dark));
    display: flex;
    flex-direction: column;
    align-items: center;
    justify-content: center;
    text-align: center;
  }
  .card-back .brand-name { color: var(--white); font-size: 24px; }
  .card-back .brand-mark { background: var(--white); width: 18px; height: 18px; }
  .card-back .brand-tagline { color: var(--white); margin-top: 10px; }
</style>
</head>
<body>
  <section class="card card-front">
    <div class="contact">
      <h1 class="contact-name">TLENZ HANDYMAN</h1>
      <p class="contact-role">Owner</p>
      <ul class="contact-lines">
        <li>PO Box 8172</li>
        <li>Hilo, Hawaii 96738</li>
        <li>808 555 0147</li>
        <li>tlenz8172@mailvexa.com</li>
      </ul>
    </div>
    <div class="front-brand">
      <div class="brand-name"><span class="brand-mark"></span><span>TL Handymand<br>and Landscaping</span></div>
      <p class="brand-tagline">QUALITY WORK, FAIR PRICE</p>
    </div>
    <div class="front-band"></div>
  </section>

  <section class="card card-back">
    <div class="brand-name"><span class="brand-mark"></span><span>TL Handymand<br>and Landscaping</span></div>
    <p class="brand-tagline">QUALITY WORK, FAIR PRICE</p>
  </section>
</body>
</html>
```